Bright Reed Yellow Perch Fish Stock and immune system boosts

We are a non-profit that sets up Aquaponics's systems in cities of 5000 or less in the Midwest. We have created a product that uses our yellow perch carcasses as the base for this broth. Our fish are grown in containment from egg to market size fish. This means it is the safest most sustainable product on the market. We also use veggies grown in the same aquaponics system network. One product has oriental overtones and mixed with antioxidants as a gut immune system bacteria booster. The other is a standard broth that has multiple uses. We are looking for packaging for both our broths. We have included our logo (a pixel guild creation). This product packaging will also be a media piece promoting The Bright Reed way of life and a way to raise revenue for the non-profit. We have not chosen the names of products but will be under the "Bright Reed" verbiage. Example is " "Bright Reed Trout Tide stock"
I have added some current examples of packaging

Target Market(s)

consumers and commercial clients

Industry/Entity Type

Grocery Store

Colors

Designer to choose colors to be used in the design.

Requirements
Must have
• Fresh feeling, restorative qualities, safe, sustainable
• Package size is 32 oz. shape is flexible

```html
<!DOCTYPE html>
<html lang="en">
<head>
<meta charset="utf-8">
<title>Bright Reed Trout TideStock – Carton</title>
<link rel="stylesheet" href="https://fonts.googleapis.com/css2?family=Marcellus+SC&family=PT+Sans+Narrow:wght@400;700&family=Montserrat:wght@600;700&display=swap">
<style>
  :root {
    --backdrop: #ebebeb;
    --teal-deep: #1d5566;
    --teal-mid: #2c7391;
    --orange: #e6840e;
    --orange-soft: #f0a53a;
    --cream: #fff6e6;
    --white: #ffffff;
  }
  * { box-sizing: border-box; margin: 0; padding: 0; }
  html, body { width: 978px; height: 1200px; overflow: hidden; background: var(--backdrop); }
  .carton {
    position: absolute; left: 29px; top: 60px;
    width: 920px; height: 1080px;
    display: flex;
  }
  .panel { position: relative; height: 100%; overflow: hidden; }
  .panel--side { width: 300px; }
  .panel--front { width: 620px; }
  .pattern-field {
    position: absolute; inset: 0;
    background:
      radial-gradient(circle at 30% 25%, rgba(240,165,58,.55), transparent 45%),
      radial-gradient(circle at 75% 70%, rgba(230,132,14,.5), transparent 45%),
      linear-gradient(160deg, var(--teal-mid), var(--teal-deep));
  }
  .panel--side .pattern-field { filter: brightness(.9); }

  /* side panel */
  .side-label {
    position: absolute; left: 32px; top: 130px; width: 236px; height: 900px;
    background: var(--orange);
    color: var(--cream);
    text-align: center;
    padding: 56px 22px 0;
  }
  .side-title {
    font-family: "Marcellus SC", serif; font-weight: 400;
    font-size: 32px; line-height: 1.15; color: var(--cream);
  }
  .rule { display: block; margin: 8px auto; height: 1px; background: var(--cream); }
  .rule--short { width: 110px; }
  .rule--long { width: 160px; }
  .side-copy {
    font-family: "PT Sans Narrow", sans-serif;
    font-size: 15.5px; line-height: 1.35;
    margin-top: 44px;
  }
  .side-copy p + p { margin-top: 20px; }
  .side-copy .kicker { display: block; }

  /* front panel */
  .brand-mark {
    position: absolute; left: 50%; top: 14px; transform: translateX(-50%);
    width: 130px; height: 130px; border-radius: 50%;
    background: var(--orange);
  }
  .front-label {
    position: absolute; left: 46px; top: 120px; width: 528px; height: 910px;
    background: var(--orange);
    color: var(--white);
    text-align: center;
  }
  .brand-name {
    position: absolute; left: 0; right: 0; top: 66px;
    font-family: "Marcellus SC", serif; font-size: 30px; color: var(--cream);
    line-height: 1;
  }
  .brand-region {
    position: absolute; left: 0; right: 0; top: 100px;
    font-family: "Marcellus SC", serif; font-size: 14px; color: var(--cream);
  }
  .title-rule {
    position: absolute; height: 1px; background: var(--cream);
  }
  .title-rule--top { left: 110px; width: 308px; top: 160px; }
  .title-rule--bottom { left: 50px; width: 428px; top: 352px; }
  .product-title {
    position: absolute; left: 0; right: 0; top: 176px;
    font-family: "Marcellus SC", serif; font-weight: 400;
    font-size: 66px; line-height: 1.2; color: var(--cream);
  }
  .claim-seal { position: absolute; left: 64px; top: 400px; width: 400px; height: 300px; overflow: visible; }
  .fish-illustration {
    position: absolute; left: 144px; top: 462px; width: 240px; height: 150px;
    border-radius: 50%;
    background: radial-gradient(ellipse at center, rgba(255,255,255,.28), rgba(255,255,255,.06));
  }
  .natural-badge {
    position: absolute; left: 237px; top: 722px;
    width: 54px; height: 54px; border-radius: 50%;
    background: var(--teal-deep); border: 3px solid var(--white);
  }
  .concentrate {
    position: absolute; left: 0; right: 0; top: 838px;
    font-family: "Montserrat", sans-serif; font-weight: 700;
    font-size: 17px; letter-spacing: .2px; color: var(--white);
  }
</style>
</head>
<body>
  <main class="carton">
    <section class="panel panel--side">
      <div class="pattern-field" role="img" aria-label="Repeating pattern of small orange and blue fish on a teal ground"></div>
      <div class="side-label">
        <span class="rule rule--short"></span>
        <h2 class="side-title">Trout<br>TideStock</h2>
        <span class="rule rule--long"></span>
        <div class="side-copy">
          <p><span class="kicker">THIS IS DUMMY TEXT</span>We are a non-profit that sets up Aquaponics's systems in cities of 5000 or less in the Midwest. We have created a product that uses our yellow perch carcasses as the base for this broth. Our fish are grown in containment from egg to market size fish.</p>
          <p><span class="kicker">THIS IS DUMMY TEXT</span>This means it is the safest most sustainable product on the market. We also use veggies grown in the same aquaponics system network. One product has oriental overtones and mixed with antioxidants as a gut immune system bacteria booster.</p>
          <p><span class="kicker">THIS IS DUMMY TEXT</span>This product packaging will also be a media piece promoting The Bright Reed way of life and a way to raise revenue for the non-profit. We have not chosen the names of products but will be under the "Bright Reed" verbiage. Example is " "Bright Reed Trout Tide stock"</p>
        </div>
      </div>
    </section>

    <section class="panel panel--front">
      <div class="pattern-field" role="img" aria-label="Repeating pattern of small orange and blue fish on a teal ground"></div>
      <div class="brand-mark"></div>
      <div class="front-label">
        <p class="brand-name">Bright Reed</p>
        <p class="brand-region">Great Lakes Region</p>
        <span class="title-rule title-rule--top"></span>
        <h1 class="product-title">Trout<br>TideStock</h1>
        <span class="title-rule title-rule--bottom"></span>
        <div class="fish-illustration" role="img" aria-label="White line drawing of a perch"></div>
        <svg class="claim-seal" viewBox="0 0 400 300" aria-label="Rich in antioxidants and gut friendly probiotics">
          <defs>
            <path id="arc-top" d="M70 150 A130 130 0 0 1 330 150"/>
            <path id="arc-bottom" d="M50 130 A150 150 0 0 0 350 130"/>
          </defs>
          <text font-family="Montserrat, sans-serif" font-weight="600" font-size="16" letter-spacing="2" fill="#ffffff">
            <textPath href="#arc-top" startOffset="50%" text-anchor="middle">RICH IN ANTIOXIDANTS</textPath>
          </text>
          <text font-family="Montserrat, sans-serif" font-weight="600" font-size="16" letter-spacing="2" fill="#ffffff">
            <textPath href="#arc-bottom" startOffset="50%" text-anchor="middle">AND GUT FRIENDLY PROBIOTICS</textPath>
          </text>
        </svg>
        <div class="natural-badge"></div>
        <p class="concentrate">CONCENTERATED</p>
      </div>
    </section>
  </main>
</body>
</html>
```